web page look and feel - B2B enterprise application

We have an enterprise application with 10 to 15 core pages and several supporting pages or popups. To start, we want the graphical design of the Users, Roles and Data Source pages and their supporting popups, wizards, etc. to be made beautiful. That is around 10 pages in total. There is a fair amount of redundancy among the pages. I have attached 5 screenshots. We very much want the pages to project a premium feel. That is absolutely essential. The color scheme is blue and sometimes yellow (only if it makes the page look better) plus black, gray and white. If the design of these screens goes well, we would expand the project to continue with other pages. The core of what we are looking for is graphic in nature but we are open to workflow suggestions if you have them. The Roles screen needs some improvements to the layout. I am looking for everything that includes icons, fonts, spacing, etc. I assume getting to the final design will take some back and forth with multiple revisions.

Target Market(s)

Large Enterprises

Number of Pages Required

5+ page

Requirements
Must have
• Premium feel

```html
<!DOCTYPE html>
<html lang="en">
<head>
<meta charset="utf-8">
<title>Users – Norvale Data</title>
<link href="https://fonts.googleapis.com/css2?family=Lato:wght@400;700&family=Montserrat:wght@400;500;600&display=swap" rel="stylesheet">
<style>
:root{
  --navy:#0c213d;
  --navy-band:#1a3454;
  --brand-a:#1a6ae8;
  --brand-b:#0a2c9c;
  --blue:#2a8af0;
  --blue-deep:#1668d8;
  --blue-soft:#6fb2f5;
  --icon-blue:#4a9ae8;
  --line:#b9d8f7;
  --page:#ececec;
  --white:#ffffff;
  --ink:#444a52;
  --title:#555a60;
  --muted:#c9d1db;
  --ok:#1fcf8e;
}
*{box-sizing:border-box;margin:0;padding:0}
html,body{width:1200px;height:786px;overflow:hidden}
body{position:relative;background:var(--page);font-family:'Lato',sans-serif;color:var(--ink)}
svg{display:block}

/* sidebar */
.sidebar{position:absolute;left:0;top:0;width:300px;height:786px;background:var(--navy);color:var(--white)}
.brand{height:80px;background:linear-gradient(90deg,var(--brand-a),var(--brand-b));display:flex;align-items:center;padding-left:64px;gap:10px}
.brand-dot{width:18px;height:18px;border-radius:50%;background:var(--white)}
.brand-name{font-family:'Montserrat',sans-serif;font-weight:600;font-size:24px;color:var(--white)}
.profile{position:absolute;top:100px;left:40px;display:flex;gap:10px;align-items:center}
.avatar{width:40px;height:40px;border-radius:50%;background:linear-gradient(135deg,#c9a38a,#5b4a42);border:2px solid #e8e8e8}
.profile-name{font-family:'Montserrat',sans-serif;font-size:15px;font-weight:500}
.profile-mail{font-family:'Montserrat',sans-serif;font-size:12px;color:var(--muted);margin-top:3px}
.side-rule{position:absolute;top:160px;left:20px;width:260px;height:1px;background:#2c4564}
.nav{position:absolute;top:176px;left:20px;width:280px;list-style:none}
.nav-item{height:32px;display:flex;align-items:center;font-size:14px;position:relative;padding-left:20px;gap:14px}
.nav-item.open{background:var(--navy-band);border-right:4px solid var(--blue)}
.nav-item.sub{padding-left:44px;gap:8px}
.nav-item .chev{position:absolute;right:36px}
.nav-item .spacer{height:32px}
.clock-row{position:absolute;top:658px;left:32px;width:240px;display:flex;justify-content:space-between;font-family:'Montserrat',sans-serif;font-size:14px;font-weight:500}
.clock-row span{display:flex;align-items:center;gap:10px}

/* header */
.topbar{position:absolute;left:300px;top:0;width:900px;height:80px;background:var(--white);border-bottom:1px solid var(--blue)}
.topbar > *{position:absolute}
.user-menu{left:742px;top:27px;display:flex;align-items:center;gap:12px;font-family:'Montserrat',sans-serif;font-weight:600;font-size:16px;color:var(--blue-deep)}

/* content */
.page-title{position:absolute;left:329px;top:116px;font-family:'Montserrat',sans-serif;font-weight:400;font-size:31px;color:var(--title)}
.search{position:absolute;left:1092px;top:99px;display:flex;gap:8px;align-items:center;color:var(--icon-blue);font-size:16px}
.btn-add{position:absolute;left:1105px;top:140px;width:64px;height:29px;background:var(--blue-deep);color:var(--white);border-radius:3px;display:flex;align-items:center;justify-content:center;gap:6px;font-size:15px;box-shadow:0 2px 6px rgba(22,104,216,.45)}

.grid{position:absolute;left:330px;width:840px;background:var(--white);border:1px solid var(--line)}
.row{display:grid;grid-template-columns:40px 137px 137px 137px 137px 137px 1fr;height:39px}
.row > div{display:flex;align-items:center;justify-content:center;border-right:1px solid var(--line);border-bottom:1px solid var(--line);font-size:15px}
.row > div:last-child{border-right:0}
.row.head > div{background:var(--blue);color:var(--white);font-size:16px;border-color:#7cb9f5}
.actions{gap:10px}
.act{width:20px;height:19px;background:var(--icon-blue);border-radius:2px;display:flex;align-items:center;justify-content:center}

.detail{display:grid;grid-template-columns:419px 1fr}
.detail > div{height:39px;display:flex;align-items:center;justify-content:center;font-size:15px;border-bottom:1px solid var(--line);gap:6px}
.detail > div:nth-child(odd){border-right:1px solid var(--line)}
.detail .dh{background:var(--blue);color:var(--white);border-color:#7cb9f5}
.perm{display:flex;align-items:center;gap:6px;margin:0 9px}
.edit-bar{height:39px;background:var(--blue-soft);color:var(--white);display:flex;align-items:center;justify-content:center;font-weight:700;font-size:15px}

.pager{position:absolute;left:677px;top:731px;display:flex;align-items:center;gap:6px;color:var(--blue-soft);font-size:15px}
.pager .cur{color:var(--blue)}
.page-size{margin-left:14px;background:var(--blue-soft);color:var(--white);font-weight:700;padding:1px 6px;font-size:14px;display:flex;gap:3px;align-items:center}
</style>
</head>
<body>

<aside class="sidebar">
  <div class="brand"><span class="brand-dot"></span><span class="brand-name">Norvale Data</span></div>
  <div class="profile">
    <div class="avatar" role="img" aria-label="User profile photo"></div>
    <div><div class="profile-name">Dana Rowe</div><div class="profile-mail">dana.rowe@example.com</div></div>
  </div>
  <div class="side-rule"></div>
  <ul class="nav">
    <li class="nav-item open"><svg width="18" height="18" viewBox="0 0 18 18"><circle cx="9" cy="5" r="4" fill="#2a8af0"/><path d="M1 18c0-5 3.5-7 8-7s8 2 8 7z" fill="#2a8af0"/></svg>User<svg class="chev" width="10" height="6" viewBox="0 0 10 6"><path d="M1 1l4 4 4-4" stroke="#fff" fill="none"/></svg></li>
    <li class="nav-item sub"><svg width="16" height="16" viewBox="0 0 16 16"><circle cx="8" cy="5" r="3.5" stroke="#fff" fill="none"/><path d="M1.5 15c0-4 3-5.5 6.5-5.5s6.5 1.5 6.5 5.5z" stroke="#fff" fill="none"/></svg>Roles</li>
    <li class="nav-item sub"><svg width="16" height="16" viewBox="0 0 16 16"><path d="M3 12V7a5 5 0 0110 0v5l1.5 1.5h-13z M6.5 14.5a1.5 1.5 0 003 0" stroke="#fff" fill="none"/></svg>Notification Groups</li>
    <li class="nav-item open" style="margin-top:-1px"><svg width="18" height="16" viewBox="0 0 18 16"><rect x="1" y="1" width="16" height="5" fill="#2a8af0"/><rect x="1" y="8" width="16" height="5" fill="#2a8af0"/><path d="M9 13v3M3 15.5h12" stroke="#2a8af0"/></svg>Data Source<svg class="chev" width="10" height="6" viewBox="0 0 10 6"><path d="M1 1l4 4 4-4" stroke="#fff" fill="none"/></svg></li>
    <li class="nav-item sub"><svg width="18" height="16" viewBox="0 0 18 16"><path d="M6 1h10v14H6M1 8h10M8 5l3 3-3 3" stroke="#fff" fill="none"/></svg>Data Object Relationship</li>
    <li class="nav-item"><svg width="18" height="18" viewBox="0 0 18 18"><rect x="0" y="0" width="8" height="18" fill="#fff"/><rect x="10" y="0" width="8" height="8" fill="#fff"/><rect x="10" y="10" width="8" height="8" fill="#fff"/></svg>Data Sets</li>
    <li class="nav-item"><svg width="18" height="18" viewBox="0 0 18 18"><rect x="0" y="0" width="7" height="18" fill="#fff"/><path d="M9 2h9M9 6h9M9 10h9M9 14h9" stroke="#fff" stroke-width="2"/></svg>Rule Sets</li>
    <li class="nav-item"><svg width="18" height="18" viewBox="0 0 18 18"><circle cx="9" cy="9" r="8" stroke="#fff" stroke-width="2" fill="none"/><path d="M9 4v5l3 2" stroke="#fff" stroke-width="2" fill="none"/></svg>Schedule</li>
    <li class="nav-item open"><svg width="18" height="18" viewBox="0 0 18 18"><path d="M2 8a7 7 0 0113-2M16 10a7 7 0 01-13 2" stroke="#2a8af0" stroke-width="2" fill="none"/><path d="M15 2v5h-5M3 16v-5h5" stroke="#2a8af0" stroke-width="2" fill="none"/></svg>Metadata Import/Export<svg class="chev" width="10" height="6" viewBox="0 0 10 6"><path d="M1 1l4 4 4-4" stroke="#fff" fill="none"/></svg></li>
    <li class="nav-item sub"><svg width="12" height="16" viewBox="0 0 12 16"><path d="M6 1v14M1 10l5 5 5-5" stroke="#fff" fill="none"/></svg>Import</li>
    <li class="nav-item sub"><svg width="12" height="16" viewBox="0 0 12 16"><path d="M6 15V1M1 6l5-5 5 5" stroke="#fff" fill="none"/></svg>Export</li>
  </ul>
  <div class="clock-row">
    <span><svg width="24" height="26" viewBox="0 0 24 26"><rect x="1" y="4" width="22" height="21" rx="2" stroke="#fff" stroke-width="2" fill="none"/><path d="M1 9h22M6 1v5M18 1v5" stroke="#fff" stroke-width="2"/><text x="12" y="22" font-size="11" font-weight="700" text-anchor="middle" fill="#fff" font-family="Montserrat, sans-serif">5</text></svg>July 05</span>
    <span><svg width="24" height="24" viewBox="0 0 24 24"><circle cx="12" cy="12" r="11" stroke="#fff" stroke-width="2" fill="none"/><path d="M12 5v7h5" stroke="#fff" stroke-width="2" fill="none"/></svg>18:36</span>
  </div>
</aside>

<header class="topbar">
  <svg style="left:30px;top:31px" width="19" height="17" viewBox="0 0 19 17"><path d="M0 2h19M0 8.5h19M0 15h19" stroke="#1668d8" stroke-width="3"/></svg>
  <svg style="left:493px;top:30px" width="26" height="20" viewBox="0 0 26 20"><path d="M3 17a10 10 0 1120 0" stroke="#1668d8" stroke-width="3" fill="none"/><path d="M13 17l5-7" stroke="#1668d8" stroke-width="3"/></svg>
  <svg style="left:543px;top:28px" width="26" height="26" viewBox="0 0 26 26"><path d="M2 24L17 9" stroke="#1668d8" stroke-width="3"/><path d="M20 2v4M18 4h4M24 10v3M22.5 11.5h3M13 1v3M11.5 2.5h3" stroke="#1668d8" stroke-width="1.5"/></svg>
  <svg style="left:593px;top:28px" width="26" height="26" viewBox="0 0 26 26"><circle cx="12" cy="12" r="12" fill="#4a9ae8"/><text x="12" y="18" font-size="17" font-weight="700" text-anchor="middle" fill="#fff" font-family="Lato, sans-serif">?</text></svg>
  <svg style="left:643px;top:28px" width="28" height="26" viewBox="0 0 28 26"><circle cx="10" cy="15" r="7" stroke="#1668d8" stroke-width="4" stroke-dasharray="3 2.5" fill="none"/><circle cx="10" cy="15" r="2.5" fill="#1668d8"/><circle cx="21" cy="7" r="4.5" stroke="#1668d8" stroke-width="3" stroke-dasharray="2.5 2" fill="none"/></svg>
  <div class="user-menu">
    <svg width="20" height="24" viewBox="0 0 20 24"><circle cx="10" cy="6" r="5.5" fill="#1668d8"/><path d="M0 24c0-7 4-10 10-10s10 3 10 10z" fill="#1668d8"/></svg>
    Dana Rowe
    <svg style="margin-left:10px" width="11" height="7" viewBox="0 0 11 7"><path d="M1 1l4.5 4.5L10 1" stroke="#1668d8" stroke-width="1.5" fill="none"/></svg>
  </div>
</header>

<main>
  <h1 class="page-title">Users</h1>
  <div class="search">Search <svg width="22" height="22" viewBox="0 0 22 22"><circle cx="9" cy="9" r="7.5" stroke="#4a9ae8" stroke-width="2" fill="none"/><path d="M14.5 14.5l6 6" stroke="#4a9ae8" stroke-width="2"/></svg></div>
  <div class="btn-add"><svg width="16" height="16" viewBox="0 0 16 16"><circle cx="8" cy="8" r="7" stroke="#fff" stroke-width="1.5" fill="none"/><path d="M8 4v8M4 8h8" stroke="#fff" stroke-width="1.5"/></svg>Add</div>

  <section class="grid" style="top:188px">
    <div class="row head"><div></div><div>First Name</div><div>Last Name</div><div>Username</div><div>Email</div><div>Status</div><div>Edit</div></div>
    <div class="row">
      <div><svg width="7" height="11" viewBox="0 0 7 11"><path d="M1 1l4.5 4.5L1 10" stroke="#4a9ae8" stroke-width="2" fill="none"/></svg></div>
      <div>Test</div><div>Test</div><div>test.1</div><div>test@example.com</div><div>Active</div>
      <div class="actions"><span class="act"><svg width="12" height="12" viewBox="0 0 12 12"><path d="M2 10l1-3 5-5 2 2-5 5zM1 11.5h10" stroke="#fff" fill="none"/></svg></span><span class="act"><svg width="12" height="12" viewBox="0 0 12 12"><rect x="1" y="3" width="7" height="8" stroke="#fff" fill="none"/><path d="M4 3V1h7v7H8" stroke="#fff" fill="none"/></svg></span><span class="act"><svg width="12" height="12" viewBox="0 0 12 12"><path d="M1 2.5h10M4 2.5V1h4v1.5M2.5 2.5l.7 9h5.6l.7-9M5 5v5M7 5v5" stroke="#fff" fill="none"/></svg></span></div>
    </div>
    <div class="detail">
      <div class="dh">Object</div><div class="dh">Permissions</div>
      <div>System Settings</div>
      <div><span class="perm"><svg width="20" height="20" viewBox="0 0 20 20"><circle cx="10" cy="10" r="10" fill="#1fcf8e"/><path d="M5 10l3.5 3.5L15 7" stroke="#fff" stroke-width="2.5" fill="none"/></svg>Read</span><span class="perm"><svg width="20" height="20" viewBox="0 0 20 20"><circle cx="10" cy="10" r="10" fill="#1fcf8e"/><path d="M5 10l3.5 3.5L15 7" stroke="#fff" stroke-width="2.5" fill="none"/></svg>Write</span></div>
      <div>Users</div>
      <div><span class="perm"><svg width="20" height="20" viewBox="0 0 20 20"><circle cx="10" cy="10" r="10" fill="#1fcf8e"/><path d="M5 10l3.5 3.5L15 7" stroke="#fff" stroke-width="2.5" fill="none"/></svg>Read</span><span class="perm"><svg width="20" height="20" viewBox="0 0 20 20"><circle cx="10" cy="10" r="10" fill="#1fcf8e"/><path d="M5 10l3.5 3.5L15 7" stroke="#fff" stroke-width="2.5" fill="none"/></svg>Write</span></div>
      <div class="dh">Data Source</div><div class="dh">Role</div>
      <div>All Data Sources</div><div>All Administrator</div>
    </div>
    <div class="edit-bar">Edit</div>
  </section>

  <section class="grid" style="top:511px;border-bottom:0">
    <div class="row"><div><svg width="11" height="7" viewBox="0 0 11 7"><path d="M1 1l4.5 4.5L10 1" stroke="#4a9ae8" stroke-width="2" fill="none"/></svg></div><div>Test</div><div>Test</div><div>test.1</div><div>test@example.com</div><div>Active</div><div class="actions"><span class="act"><svg width="12" height="12" viewBox="0 0 12 12"><path d="M2 10l1-3 5-5 2 2-5 5zM1 11.5h10" stroke="#fff" fill="none"/></svg></span><span class="act"><svg width="12" height="12" viewBox="0 0 12 12"><rect x="1" y="3" width="7" height="8" stroke="#fff" fill="none"/><path d="M4 3V1h7v7H8" stroke="#fff" fill="none"/></svg></span><span class="act"><svg width="12" height="12" viewBox="0 0 12 12"><path d="M1 2.5h10M4 2.5V1h4v1.5M2.5 2.5l.7 9h5.6l.7-9M5 5v5M7 5v5" stroke="#fff" fill="none"/></svg></span></div></div>
    <div class="row"><div><svg width="11" height="7" viewBox="0 0 11 7"><path d="M1 1l4.5 4.5L10 1" stroke="#4a9ae8" stroke-width="2" fill="none"/></svg></div><div>Test</div><div>Test</div><div>test.1</div><div>test@example.com</div><div>Active</div><div class="actions"><span class="act"><svg width="12" height="12" viewBox="0 0 12 12"><path d="M2 10l1-3 5-5 2 2-5 5zM1 11.5h10" stroke="#fff" fill="none"/></svg></span><span class="act"><svg width="12" height="12" viewBox="0 0 12 12"><rect x="1" y="3" width="7" height="8" stroke="#fff" fill="none"/><path d="M4 3V1h7v7H8" stroke="#fff" fill="none"/></svg></span><span class="act"><svg width="12" height="12" viewBox="0 0 12 12"><path d="M1 2.5h10M4 2.5V1h4v1.5M2.5 2.5l.7 9h5.6l.7-9M5 5v5M7 5v5" stroke="#fff" fill="none"/></svg></span></div></div>
    <div class="row"><div><svg width="11" height="7" viewBox="0 0 11 7"><path d="M1 1l4.5 4.5L10 1" stroke="#4a9ae8" stroke-width="2" fill="none"/></svg></div><div>Test</div><div>Test</div><div>test.1</div><div>test@example.com</div><div>Active</div><div class="actions"><span class="act"><svg width="12" height="12" viewBox="0 0 12 12"><path d="M2 10l1-3 5-5 2 2-5 5zM1 11.5h10" stroke="#fff" fill="none"/></svg></span><span class="act"><svg width="12" height="12" viewBox="0 0 12 12"><rect x="1" y="3" width="7" height="8" stroke="#fff" fill="none"/><path d="M4 3V1h7v7H8" stroke="#fff" fill="none"/></svg></span><span class="act"><svg width="12" height="12" viewBox="0 0 12 12"><path d="M1 2.5h10M4 2.5V1h4v1.5M2.5 2.5l.7 9h5.6l.7-9M5 5v5M7 5v5" stroke="#fff" fill="none"/></svg></span></div></div>
    <div class="row"><div><svg width="11" height="7" viewBox="0 0 11 7"><path d="M1 1l4.5 4.5L10 1" stroke="#4a9ae8" stroke-width="2" fill="none"/></svg></div><div>Test</div><div>Test</div><div>test.1</div><div>test@example.com</div><div>Active</div><div class="actions"><span class="act"><svg width="12" height="12" viewBox="0 0 12 12"><path d="M2 10l1-3 5-5 2 2-5 5zM1 11.5h10" stroke="#fff" fill="none"/></svg></span><span class="act"><svg width="12" height="12" viewBox="0 0 12 12"><rect x="1" y="3" width="7" height="8" stroke="#fff" fill="none"/><path d="M4 3V1h7v7H8" stroke="#fff" fill="none"/></svg></span><span class="act"><svg width="12" height="12" viewBox="0 0 12 12"><path d="M1 2.5h10M4 2.5V1h4v1.5M2.5 2.5l.7 9h5.6l.7-9M5 5v5M7 5v5" stroke="#fff" fill="none"/></svg></span></div></div>
    <div class="row"><div><svg width="11" height="7" viewBox="0 0 11 7"><path d="M1 1l4.5 4.5L10 1" stroke="#4a9ae8" stroke-width="2" fill="none"/></svg></div><div>Test</div><div>Test</div><div>test.1</div><div>test@example.com</div><div>Active</div><div class="actions"><span class="act"><svg width="12" height="12" viewBox="0 0 12 12"><path d="M2 10l1-3 5-5 2 2-5 5zM1 11.5h10" stroke="#fff" fill="none"/></svg></span><span class="act"><svg width="12" height="12" viewBox="0 0 12 12"><rect x="1" y="3" width="7" height="8" stroke="#fff" fill="none"/><path d="M4 3V1h7v7H8" stroke="#fff" fill="none"/></svg></span><span class="act"><svg width="12" height="12" viewBox="0 0 12 12"><path d="M1 2.5h10M4 2.5V1h4v1.5M2.5 2.5l.7 9h5.6l.7-9M5 5v5M7 5v5" stroke="#fff" fill="none"/></svg></span></div></div>
  </section>

  <nav class="pager">
    <svg width="7" height="11" viewBox="0 0 7 11"><path d="M6 1L1.5 5.5 6 10" stroke="#2a8af0" stroke-width="2" fill="none"/></svg>
    <span class="cur">1</span><span>2</span><span>3</span><span>4</span>
    <svg style="margin-left:6px" width="7" height="11" viewBox="0 0 7 11"><path d="M1 1l4.5 4.5L1 10" stroke="#2a8af0" stroke-width="2" fill="none"/></svg>
    <span class="page-size">20<svg width="7" height="5" viewBox="0 0 7 5"><path d="M1 1l2.5 2.5L6 1" stroke="#fff" fill="none"/></svg></span>
  </nav>
</main>

</body>
</html>
```